Flyer needed to promote gutter clearance service for established gardening company

We need a bright and engaging flyer to be designed to advertise our gutter clearance service.
Whilst we are a gardening company that normally does more horticultural work, during the winter we offer other services such as gutter clearance where we remove the debris from gutters and thereby reducing the risk of clogs, leakage, breakage and potential structural damage to the property.

Full details of our service, together with our overall brand and colours can be seen on www.marlowtreecare.co.uk/gutters.

We would like you to use the page on the website as a basis to create the flyer and so please feel free to use as much or as little of the wording contained within the webpage on the flyer drawing particular attention to "Prices starting at just £60 for an average 3 bed house". I will upload pictures but please feel free to use other graphics and fonts to make it stand out.

The contact details which should be included within the flyer are as follows:

Marlow Treecare Services Ltd
Orbit Trading Centre
Fairbrook Vale Ind Estate
Swindon
SN4 7HW

Tel: 01793 418302
www.marlowtreecare.co.uk
dean@marlowtreecare.co.uk

The flyers will eventually be printed out in A5 (210mm x 148mm) using Printelle and so needs to be in that size and suitable file for upload.

I have only put this as a 2 day project as its really urgent and I'm hoping we get some great designs in that time.

Target Market(s)

Homeowners between 25 - 65+

Industry/Entity Type

Home Improvement

Font styles to use
Serif
Sans Serif
Decorative
Script

Colors
6b449b
9bcb3c

Requirements
Must have
• Our colours are purple and green as seen on our website www.marlowtreecare.co.uk/gutters. Please use those colours.
• The flyer should draw attention to the following facts:
• We are Marlow Treecare Services Ltd (see attached logo)
• We are offering a Gutter Clearance Service in Swindon
• Prices start at just £60 for the average 3 bed house.
• We are fully insured.
• Our contact details must be included (as in the product description above)
• I have attached pictures but feel free to add other graphics or use fonts to make the flyer more engaging and interesting.
• Additional wording may be taken from the website at the address shown above. You can use as much or as little wording as you like just as long as the message gets across and the flyer contains our contact information and logo and the details shown above.
Nice to have
• I would like a bright and modern design which isn't too busy or cluttered. It should be something that is quick and easy to read.
Should not have
• I don't want it to look too busy or crowded with small type which people just won't read. Whilst I've said you can take whatever wording you want from our website, I'd suggest you don't take it all or too much. I want the main message (as detailed above in 'must haves') to stand out rather than have it contained deep within lots of small type face.

```html
<!DOCTYPE html>
<html lang="en">
<head>
<meta charset="utf-8">
<title>Gutter Clearance Services – Marlow Treecare Services</title>
<link rel="stylesheet" href="https://fonts.googleapis.com/css2?family=Montserrat:wght@700;800&family=Quicksand:wght@500;700&display=swap">
<style>
  :root {
    --green-dark: #6fa61c;
    --green-mid: #8cc43a;
    --green-light: #a9d655;
    --purple: #6b449b;
    --purple-edge: #8a63bd;
    --ink: #1c1c1c;
    --brown: #3a2418;
    --brand-green: #5cb82e;
    --white: #ffffff;
  }
  * { margin: 0; padding: 0; box-sizing: border-box; }
  html, body { width: 846px; height: 1200px; overflow: hidden; background: #fff; }
  .flyer {
    position: relative; width: 846px; height: 1200px; overflow: hidden;
    font-family: "Quicksand", sans-serif; color: var(--ink);
    background: linear-gradient(180deg, #f4f4f4 0%, #ffffff 40%, #ececec 100%);
  }
  .hero {
    position: absolute; left: 0; top: 0; width: 846px; height: 940px;
    background: radial-gradient(ellipse at 35% 30%, var(--green-light) 0%, var(--green-mid) 55%, var(--green-dark) 100%);
  }
  .hero-step {
    position: absolute; left: 0; top: 0; width: 846px; height: 940px;
  }
  .title {
    position: absolute; left: 32px; top: 30px;
    font-family: "Montserrat", sans-serif; font-weight: 800;
    font-size: 58px; letter-spacing: -0.5px; color: var(--ink); white-space: nowrap;
  }
  .intro { position: absolute; left: 33px; top: 110px; width: 450px; }
  .intro h2 {
    font-family: "Montserrat", sans-serif; font-weight: 700;
    font-size: 19.5px; margin-bottom: 6px;
  }
  .intro p {
    font-size: 17.6px; line-height: 22.4px; font-weight: 500;
    text-align: justify; margin-bottom: 5px;
  }
  .help {
    position: absolute; left: 506px; top: 120px; width: 322px; height: 476px;
    background: var(--purple); border: 4px solid var(--purple-edge);
    color: var(--white); padding: 8px 18px 0 18px;
  }
  .help h2 {
    font-family: "Montserrat", sans-serif; font-weight: 700;
    font-size: 20px; margin-bottom: 18px;
  }
  .help p { font-size: 17.6px; line-height: 23px; font-weight: 500; }
  .photo { position: absolute; }
  .photo-label {
    position: absolute; top: 6px; font-family: "Montserrat", sans-serif;
    font-weight: 700; font-size: 18px; color: var(--white);
  }
  .brand {
    position: absolute; left: 56px; top: 1040px; display: flex; align-items: center; gap: 16px;
  }
  .brand-dot { width: 44px; height: 44px; border-radius: 50%; background: var(--brand-green); }
  .brand-name {
    font-family: "Quicksand", sans-serif; font-weight: 700; font-size: 34px;
    color: var(--brown); line-height: 1.1;
  }
  .contact { position: absolute; left: 490px; top: 982px; font-size: 18.5px; font-weight: 500; }
  .contact-line { display: flex; align-items: center; gap: 10px; height: 24px; }
  .contact-line svg { width: 16px; height: 16px; flex: none; }
  .address { display: flex; gap: 10px; margin-top: 28px; font-size: 17.6px; line-height: 22px; }
  .address svg { width: 14px; height: 18px; flex: none; margin-top: 3px; }
</style>
</head>
<body>
<div class="flyer">
  <div class="hero"></div>
  <svg class="hero-step" viewBox="0 0 846 940" aria-hidden="true">
    <path d="M0 652 L528 652 L528 640 L846 612 L846 940 L0 940 Z" fill="#86bf34" opacity="0.55"/>
  </svg>

  <h1 class="title">Gutter Clearance Services</h1>

  <section class="intro">
    <h2>Why do my gutters need clearing?</h2>
    <p>Whilst you may not notice your gutters on a day to day basis, your gutters are of utmost importance as they play a key role in maintaining the structural integrity of your property. Keeping them clean and clear from debris is a great way to avoid damage to your home and potentially expensive gutter repairs.</p>
    <p>Whilst a gutter is very useful in directing rainwater from your roof and down the drain, it can accumulate leaves and moss and other debris causing it to clog and overflow or get broken. The results of this can be serious as not only could you find yourself with structural damage to tackle but it can result in damp within your home, causing potential health issues to you and your family.</p>
    <p>No matter what type of gutter you have (you may have plastic, steel or cast iron), they need to be cleaned at least once per year in order to keep them performing properly and to avoid the potential for gutter repairs in the future.</p>
  </section>

  <aside class="help">
    <h2>How can we help?</h2>
    <p>Clearing gutters is not just a dirty job but it can be a dangerous one too if not done properly. At Marlow Treecare Services, we are fully insured and use the latest tools and techniques to safely clear your gutters, giving you peace of mind without having to risk getting dirty or injured yourself. And with prices starting at just £60 to clear the gutters of an average 3 bed house, it is an affordable way to get your home prepared for the winter.</p>
  </aside>

  <div class="photo" role="img" aria-label="Gutter full of leaves before clearing" style="left:0;top:664px;width:166px;height:268px;background:linear-gradient(160deg,#6b5a48,#8b7a52 50%,#4f6a32);">
    <span class="photo-label" style="left:33px;">Before</span>
  </div>
  <div class="photo" role="img" aria-label="Clean gutter after clearing" style="left:166px;top:664px;width:168px;height:268px;background:linear-gradient(160deg,#6d5f52,#a9a497 55%,#5f8a3a);">
    <span class="photo-label" style="left:62px;">After</span>
  </div>
  <div class="photo" role="img" aria-label="Scoop lifting debris out of a gutter" style="left:345px;top:664px;width:193px;height:130px;background:linear-gradient(160deg,#d8d8d4,#8a7a5e 60%,#6f6a62);"></div>
  <div class="photo" role="img" aria-label="Gloved hands removing autumn leaves from a roof gutter" style="left:345px;top:803px;width:193px;height:129px;background:linear-gradient(160deg,#7a9a3a,#5a5e66 55%,#c89a3a);"></div>
  <div class="photo" role="img" aria-label="Worker using a leaf blower to clear a gutter" style="left:546px;top:624px;width:300px;height:308px;background:linear-gradient(150deg,#9a7a5e,#b56a4a 45%,#c8894a 80%,#e2d6c4);"></div>

  <div class="brand">
    <span class="brand-dot"></span>
    <span class="brand-name">Marlow Treecare<br>Services</span>
  </div>

  <address class="contact" style="font-style:normal;">
    <div class="contact-line">
      <svg viewBox="0 0 16 16"><path d="M3.5 1 L6 1 L7 4.5 L5.3 5.8 C6.2 7.8 8.2 9.8 10.2 10.7 L11.5 9 L15 10 L15 12.5 C15 13.9 13.9 15 12.5 15 C6.7 15 1 9.3 1 3.5 C1 2.1 2.1 1 3.5 1 Z" fill="#1c1c1c"/></svg>
      <span>01793 418302</span>
    </div>
    <div class="contact-line">
      <svg viewBox="0 0 16 16" fill="none" stroke="#1c1c1c" stroke-width="1.3"><circle cx="8" cy="8" r="6.5"/><ellipse cx="8" cy="8" rx="3" ry="6.5"/><path d="M1.5 8 H14.5 M2.5 4.8 H13.5 M2.5 11.2 H13.5"/></svg>
      <span>www.marlowtreecare.co.uk</span>
    </div>
    <div class="contact-line">
      <svg viewBox="0 0 16 16"><rect x="1" y="3.5" width="14" height="9" fill="#1c1c1c"/><path d="M1 3.5 L8 9 L15 3.5" fill="none" stroke="#fff" stroke-width="1.2"/></svg>
      <span>dean@marlowtreecare.co.uk</span>
    </div>
    <div class="address">
      <svg viewBox="0 0 14 18"><path d="M7 0 C3.1 0 0 3.1 0 7 C0 11.5 7 18 7 18 C7 18 14 11.5 14 7 C14 3.1 10.9 0 7 0 Z" fill="#1c1c1c"/><circle cx="7" cy="6.8" r="2.5" fill="#fff"/></svg>
      <span>Marlow Treecare Services Ltd<br>Orbit Trading Centre,<br>Fairbrook Vale Ind Estate,<br>Swindon, SN4 7HW</span>
    </div>
  </address>
</div>
</body>
</html>
```